New bussiness card, using company logo.
Lachlan Voss
Manager/Director
Birch Property Developments
Po Box 4657
Thuringowa Central
Qld
0455 386 218
lachlan@birchpropertydevelopments
eye catching, vibrant colours, professional

```html
<!DOCTYPE html>
<html lang="en">
<head>
<meta charset="utf-8">
<title>Birch Property Developments – Business Card</title>
<link rel="stylesheet" href="https://fonts.googleapis.com/css2?family=Oswald:wght@400&family=PT+Serif:wght@700&display=swap">
<style>
  :root {
    --brand-red: #e0252f;
    --brand-green: #6cbd45;
    --text-grey: #6d6e71;
    --card-white: #ffffff;
  }
  * { margin: 0; padding: 0; box-sizing: border-box; }
  html, body {
    width: 1200px;
    height: 686px;
    overflow: hidden;
    background: var(--card-white);
  }
  .card {
    position: relative;
    width: 1200px;
    height: 686px;
    background: var(--card-white);
    border: 14px solid var(--brand-red);
  }
  .brand {
    position: absolute;
    left: 62px;
    top: 34px;
    display: flex;
    align-items: center;
    gap: 28px;
  }
  .brand-mark {
    width: 92px;
    height: 92px;
    background: var(--brand-green);
  }
  .brand-name {
    font-family: "Oswald", sans-serif;
    font-weight: 400;
    font-size: 72px;
    line-height: 1.02;
    color: var(--brand-red);
    text-transform: uppercase;
    letter-spacing: 1px;
  }
  .person {
    position: absolute;
    left: 112px;
    top: 272px;
    display: flex;
    align-items: baseline;
    gap: 14px;
    font-family: "Oswald", sans-serif;
    font-weight: 400;
    color: var(--brand-red);
  }
  .person-name {
    font-size: 86px;
    line-height: 1;
    text-transform: uppercase;
  }
  .person-title {
    font-size: 48px;
    line-height: 1;
  }
  .contact {
    position: absolute;
    left: 112px;
    top: 404px;
    list-style: none;
    font-family: "PT Serif", serif;
    font-weight: 700;
    font-size: 49px;
    color: var(--text-grey);
  }
  .contact li { line-height: 1; white-space: nowrap; }
  .contact-address { height: 82px; }
  .contact-phone { height: 70px; }
  .contact .separator { padding: 0 14px; }
</style>
</head>
<body>
  <main class="card">
    <header class="brand">
      <span class="brand-mark" aria-hidden="true"></span>
      <p class="brand-name">Birch Property<br>Developments</p>
    </header>

    <h1 class="person">
      <span class="person-name">Lachlan Voss</span>
      <span class="person-title">Manager/Director</span>
    </h1>

    <ul class="contact">
      <li class="contact-address">PO Box 4657<span class="separator">|</span>Kestrelvale Central Vic</li>
      <li class="contact-phone">0455 386 218</li>
      <li class="contact-email">lachlan@birchpropertydevelopments</li>
    </ul>
  </main>
</body>
</html>
```